Business card to promote business guidance

I need a card design to give to all my customers advertising a way to build a business exactly like the one they just bought from. I have an online store and will include one with each shipment. It should state the way to financial freedom and working for yourself

Target Market(s)

Young Entrepreneurs that want to start and don't know how

Industry/Entity Type

Business

Contact Information for Business Card

"You just bought from a successful company on Vorpex. I have a unique business model, discovered by me, unlike any other that can make anyone successful. Follow me and message me for exactly the same model. If you ever wanted to work for yourself, I will teach you how. It's not a pipe dream, allow me to guide you out of the box."

Colors
85abd2

Requirements
Must have
• website www.loganmerewick.com
snapfolio @theloganmerewick

```html
<!DOCTYPE html>
<html lang="en">
<head>
<meta charset="utf-8">
<title>Logan Merewick – Business Card</title>
<link rel="stylesheet" href="https://fonts.googleapis.com/css2?family=Arvo&display=swap">
<style>
  :root {
    --backdrop: #1b1b1b;
    --sun-yellow: #fbc21a;
    --sun-yellow-deep: #f1a90f;
    --band-light: #fde35a;
    --band-dark: #f3b414;
    --blush-pink: #f08fa8;
    --blush-pink-light: #f5a3b8;
    --ink: #141008;
    --wine: #8e0d22;
  }
  * { margin: 0; padding: 0; box-sizing: border-box; }
  html, body {
    width: 1200px;
    height: 1200px;
    overflow: hidden;
    background: var(--backdrop);
  }
  body {
    display: flex;
    align-items: center;
    justify-content: center;
    font-family: "Arvo", "Rockwell", serif;
  }
  .business-card {
    width: 614px;
    height: 1000px;
    display: flex;
    flex-direction: column;
  }
  .message-panel {
    height: 797px;
    background: radial-gradient(ellipse at 50% 40%, var(--sun-yellow) 55%, var(--sun-yellow-deep) 100%);
    display: flex;
    flex-direction: column;
    align-items: center;
    padding-top: 74px;
  }
  .pitch {
    width: 540px;
    color: var(--ink);
    font-size: 28px;
    line-height: 52.7px;
    text-align: center;
    white-space: nowrap;
  }
  .pitch .line { display: block; }
  .flourish {
    margin-top: 14px;
    width: 122px;
    height: 52px;
  }
  .details-band {
    height: 47px;
    background: linear-gradient(to bottom, var(--band-dark) 0%, var(--band-light) 45%, var(--band-dark) 100%);
    color: var(--wine);
    font-size: 28px;
    line-height: 47px;
    text-align: center;
  }
  .contact-panel {
    height: 156px;
    background: radial-gradient(ellipse at 50% 30%, var(--blush-pink-light) 0%, var(--blush-pink) 100%);
    color: var(--ink);
    font-size: 28px;
    line-height: 40px;
    text-align: center;
    padding-top: 22px;
  }
</style>
</head>
<body>
  <div class="business-card">
    <section class="message-panel">
      <p class="pitch">
        <span class="line">You just bought from a</span>
        <span class="line">successful company on Vorpex.</span>
        <span class="line">I have a unique business model,</span>
        <span class="line">discovered by me, unlike any</span>
        <span class="line">other that can make anyone</span>
        <span class="line">successful. Follow me and</span>
        <span class="line">message me for exactly the</span>
        <span class="line">same model. If you ever wanted</span>
        <span class="line">to work for yourself, I will teach</span>
        <span class="line">you how. It's not a pipe dream,</span>
        <span class="line">allow me to guide you out</span>
        <span class="line">of the box</span>
      </p>
      <svg class="flourish" role="img" aria-label="Decorative scroll flourish ornament" viewBox="0 0 122 52">
        <ellipse cx="61" cy="30" rx="58" ry="18" fill="#2a1c05" opacity="0.18"/>
      </svg>
    </section>
    <div class="details-band">For More Details</div>
    <section class="contact-panel">
      <p class="website">www.loganmerewick.com</p>
      <p class="social-handle">snapfolio @theloganmerewick</p>
    </section>
  </div>
</body>
</html>
```